Modern Web Design for Nonprofit Organization

Our client is looking to redesign their website. They want a modern look, clean and professional, that integrates their new brand guidelines.

Here is clients current site:
http://www.valorandes.org/

They want their own unique design but here are some sites the clients likes:
https://www.brixtonvane.com/en/
https://oakhollowrise.org/
https://www.lumacraft.com/
https://www.tbnlawgroup.com/
https://www.greyharborco.org/

Attached please find the clients logos, color palette, site plan and design specs.

You will create a homepage mockup that will have the following sections in this order:
1. Thin Alert Bar at very top with one line message
2. Nav Bar with Logo and Main Nav (red in site plan)
3. Hero Image or Video
4. Signup Bar with name email and zip and connect button
5. Intro section with image, welcome message, and supporter counter
6. Featured Action section with call to action
7. Event section with two upcoming event cards
8. Latest News section with three latest blog post
9. Support our work (donation) section
10. Worker and Member Stories Section with feed of social posts
11. Footer.

You can use text and images from clients existing site or placeholder images and placeholder text.

Please submit as many home page mockups/idea boards as you like. Client will pick the top three and ask for some revisions. If you are selected this will lead to a lot of work for this client.

Project is private please adhere to ArtPlenary terms of use and do not share any materials please.

QUICKEST RESPONSE PLEASE!

Thanks for looking!

Target Market(s)

Non profit donors and farmworker advocates

Number of Pages Required

2 page

Font styles to use
Sans Serif

Requirements
Must have
• Adhere to brief and client brand ID
Nice to have
• World class design

```html
<!DOCTYPE html>
<html lang="en">
<head>
<meta charset="utf-8">
<title>Valor Andes — Nonprofit Organization</title>
<link href="https://fonts.googleapis.com/css2?family=Fira+Sans:wght@600;700;800&family=Roboto:wght@400;500;700&display=swap" rel="stylesheet">
<style>
:root{
  --red:#d0141c;
  --yellow:#fcc419;
  --ink:#1b1b1b;
  --text:#6b6b6b;
  --grey-bg:#efefef;
  --line:#dcdcdc;
  --footer:#1c1c1c;
  --white:#ffffff;
  --head:"Fira Sans",sans-serif;
  --body:"Roboto",sans-serif;
}
*{box-sizing:border-box;margin:0;padding:0}
html,body{width:1200px;height:4087px;overflow:hidden}
body{position:relative;background:var(--white);font-family:var(--body);color:var(--ink)}
.abs{position:absolute}
.photo{position:absolute;display:block}

.alert-bar{left:0;top:0;width:1200px;height:35px;background:var(--red);color:var(--white);font-size:10px;display:flex;align-items:center;justify-content:center;gap:8px}
.nav-bar{left:0;top:35px;width:1200px;height:60px;background:var(--white);display:flex;align-items:center}
.brand{position:absolute;display:flex;align-items:center;gap:8px;font-family:var(--head);font-weight:800;font-size:25px;color:var(--red)}
.brand .mark{width:16px;height:16px;background:var(--red)}
.brand.light{color:var(--white)}
.brand.light .mark{background:var(--white)}
.main-nav{position:absolute;left:413px;top:0;height:60px;display:flex;align-items:center;gap:14px;font-size:10.5px;font-weight:500;text-transform:uppercase}
.main-nav .active{border-bottom:2px solid var(--red);padding-bottom:3px}
.main-nav .drop:after{content:" ▾";font-size:8px}
.btn{position:absolute;display:flex;align-items:center;justify-content:center;gap:8px;border-radius:24px;font-weight:700;font-size:14px;text-transform:uppercase}
.btn-yellow{background:var(--yellow);color:var(--red)}
.btn-red{background:var(--red);color:var(--white)}

.hero{left:0;top:95px;width:1200px;height:573px;background:linear-gradient(180deg,#6b5a4e 0%,#8a6c5c 40%,#5a4438 100%)}
.hero-title{position:absolute;left:0;top:200px;width:1200px;text-align:center;color:var(--white);font-family:var(--head);font-weight:700;font-size:92px;line-height:98px;text-shadow:0 2px 8px rgba(0,0,0,.35)}
.signup-bar{left:0;top:590px;width:1200px;height:78px;background:rgba(20,20,20,.85)}
.signup-bar .label{position:absolute;left:143px;top:27px;color:var(--white);font-weight:700;font-size:21px}
.field{position:absolute;top:21px;height:35px;background:var(--white);font-size:10px;color:#444;padding-left:16px;display:flex;align-items:center}
.connect{position:absolute;left:955px;top:21px;width:100px;height:35px;background:var(--yellow);color:var(--red);font-weight:700;font-size:13px;display:flex;align-items:center;justify-content:center}

.section-title{position:absolute;font-family:var(--head);font-weight:700;font-size:42px;color:var(--ink)}
.center{left:0;width:1200px;text-align:center}
.copy{position:absolute;font-size:12.5px;line-height:25.6px;color:var(--text)}

.events{left:0;top:1779px;width:1200px;height:589px;background:var(--grey-bg);border-bottom:1px solid var(--line)}
.event-card{position:absolute;top:181px;width:443px;height:321px}
.event-card h3{position:absolute;left:32px;top:234px;color:var(--white);font-size:22px;font-weight:500}
.event-card .date{position:absolute;left:32px;top:274px;background:var(--red);color:var(--white);font-size:11px;font-weight:700;padding:5px 10px}
.arrow{position:absolute;width:44px;height:44px;border-radius:50%;border:1.5px solid #555;background:var(--white);display:flex;align-items:center;justify-content:center}

.post{position:absolute;top:2560px;width:287px}
.post .thumb{width:287px;height:233px}
.post h4{margin-top:28px;font-size:14.5px;font-weight:500;line-height:22px}
.post .date{position:absolute;top:340px;font-size:11.5px;color:var(--red)}
.divider{left:143px;top:2984px;width:912px;height:1px;background:var(--line)}
.partner{position:absolute;top:3166px;width:170px;height:78px;border:1px solid #bbb;background:var(--white);display:flex;align-items:center;justify-content:center}
.partner span{display:block;width:96px;height:42px;border-radius:4px}

.stories{left:0;top:3333px;width:1200px;height:465px;background:var(--grey-bg)}
.sub-title{position:absolute;font-family:var(--head);font-weight:700;font-size:21px}
.panel{position:absolute;background:var(--white);border:1px solid var(--line)}
.story{position:absolute;left:12px;width:520px}
.avatar{position:absolute;left:0;top:0;width:52px;height:52px;border-radius:50%}
.story .who{position:absolute;left:72px;top:4px;font-size:11px;font-weight:700}
.stars{color:var(--yellow);font-size:9px;margin-left:8px;letter-spacing:1px}
.story p{position:absolute;left:72px;top:26px;width:440px;font-size:10.5px;line-height:20px;font-style:italic;color:var(--text)}

.footer{left:0;top:3798px;width:1200px;height:289px;background:var(--footer);color:var(--white)}
.social{position:absolute;top:56px;width:36px;height:36px;border-radius:50%;background:var(--white)}
.call{position:absolute;left:476px;top:50px;display:flex;align-items:center;gap:14px}
.call .small{font-size:17px;font-weight:700}
.call .num{font-size:28px;font-weight:700;line-height:32px}
.footer-nav{position:absolute;left:0;top:188px;width:1200px;display:flex;justify-content:center;gap:25px;font-size:16px;font-weight:500;text-transform:uppercase}
.legal{position:absolute;left:0;top:232px;width:1200px;text-align:center;font-size:12.5px}
.foot-rule{position:absolute;left:0;top:142px;width:1200px;height:1px;background:#333}
</style>
</head>
<body>

<div class="abs alert-bar">
  <svg width="14" height="12" viewBox="0 0 14 12"><path d="M7 0L14 12H0Z" fill="#fff"/><rect x="6.3" y="4" width="1.4" height="4" fill="#d0141c"/><rect x="6.3" y="9" width="1.4" height="1.4" fill="#d0141c"/></svg>
  <span>Announcement: Corona Virus, Offices Closed to the Public 3/16 / 20-3 / 18/20</span>
</div>

<header class="abs nav-bar">
  <div class="brand" style="left:143px;top:15px"><span class="mark"></span>Valor Andes</div>
  <nav class="main-nav">
    <span class="active">Home</span><span class="drop">Get Help Now</span><span class="drop">Take Action</span><span class="drop">News and Events</span><span class="drop">Support Our Work</span><span class="drop">About Us</span>
  </nav>
  <div class="btn btn-yellow" style="left:955px;top:13px;width:100px;height:34px;font-size:12px">Donate</div>
</header>

<section class="abs hero" role="img" aria-label="Group photo of foundation staff and volunteers standing together indoors">
  <h1 class="hero-title">Nonprofit<br>Organization</h1>
</section>

<form class="abs signup-bar">
  <div class="label">SIGN UP WITH YOUR EMAIL</div>
  <div class="field" style="left:449px;width:161px">Enter Name</div>
  <div class="field" style="left:619px;width:161px">Enter Email</div>
  <div class="field" style="left:787px;width:161px">Zipcode</div>
  <div class="connect">CONNECT</div>
</form>

<section class="intro">
  <h2 class="section-title" style="left:143px;top:765px">Welcome</h2>
  <p class="copy" style="left:143px;top:840px;width:435px">The Andes Workers Foundation is a dynamic non-profit organization established in 2006. The fundamental purpose of the VA Foundation is to empower communities to ensure human dignity. We serve more than 90,000 immigrants annually through a holistic approach; we provide critical services and engage our constituents in systemic change to break the cycle of poverty. Our regional offices are havens that provide resources and services, such as credible immigration legal advice, and act as outreach centers and educational organization.</p>
  <div class="btn btn-yellow" style="left:144px;top:1074px;width:146px;height:45px">Read More</div>
  <div class="btn btn-red" style="left:300px;top:1074px;width:146px;height:45px">
    <svg width="20" height="16" viewBox="0 0 20 16"><ellipse cx="10" cy="7" rx="9.5" ry="6.5" fill="#fff"/><path d="M4 11L2 16L9 12Z" fill="#fff"/></svg>Support</div>
  <div class="photo" style="left:624px;top:725px;width:431px;height:446px;background:linear-gradient(160deg,#3b4a30,#6b5a45 55%,#2f2a26)" role="img" aria-label="Speaker at a podium addressing a seated audience"></div>
</section>

<section class="featured">
  <div class="photo" style="left:144px;top:1250px;width:432px;height:448px;background:linear-gradient(150deg,#c9c2b5,#8a7d70 50%,#3b3530)" role="img" aria-label="Community leader speaking at a podium beside a seated guest"></div>
  <h2 class="section-title" style="left:627px;top:1292px">Featured Action</h2>
  <p class="copy" style="left:627px;top:1366px;width:428px">Lorem ipsum dolor sit amet, consectetur adipiscing elit, sed do eiusmod tempor incididunt ut labore et dolore magna aliqua. Ut enim ad minim veniam, quis nostrud exercitation ullamco laboris nisi ut aliquip ex ea commodo consequais aute irure dolor in reprehenderit in voluptate velit esse cillum dolore eu fugiat nulla parixcepteur sint occaecat cupidatat non proident, sunt in culpa qui officia deserunt mollit anim id est laborumorem ipsum dolor sit amet, consectetur adipiscing elit, sed do eiusmod tempor incididunt ut labore et dolore magna aliqua.</p>
  <div class="btn btn-yellow" style="left:627px;top:1601px;width:146px;height:45px">Read More</div>
</section>

<section class="abs events">
  <h2 class="section-title center" style="top:76px">Upcoming Events</h2>
  <article class="event-card" style="left:144px">
    <div class="photo" style="inset:0;background:linear-gradient(180deg,#7a7268,#4f463f 60%,#221d1a)" role="img" aria-label="Crowd gathered at a community press event"></div>
    <h3>Lorem ipsum dolor sit ame</h3><span class="date">SEP 26,2020</span>
  </article>
  <article class="event-card" style="left:613px">
    <div class="photo" style="inset:0;background:linear-gradient(180deg,#a7a29a,#6a5f55 60%,#2a2420)" role="img" aria-label="Group holding certificates at a ceremony"></div>
    <h3>Lorem ipsum dolor sit ame</h3><span class="date">SEP 26,2020</span>
  </article>
  <div class="arrow" style="left:83px;top:319px"><svg width="12" height="18"><path d="M10 2L3 9L10 16" stroke="#333" stroke-width="2" fill="none"/></svg></div>
  <div class="arrow" style="left:1071px;top:319px"><svg width="12" height="18"><path d="M2 2L9 9L2 16" stroke="#333" stroke-width="2" fill="none"/></svg></div>
</section>

<section class="blog">
  <h2 class="section-title center" style="top:2448px">Latest Blog Post</h2>
  <article class="post" style="left:143px">
    <div class="thumb" style="background:linear-gradient(160deg,#d9c8b0,#a88e78)" role="img" aria-label="Two women holding a meal voucher"></div>
    <h4>Open Table Relief &amp; the Peasant Movement distribute meals for families of peasant workers</h4><span class="date">APR 22, 2020</span>
  </article>
  <article class="post" style="left:455px">
    <div class="thumb" style="background:linear-gradient(170deg,#3f5a2e,#2a3a20)" role="img" aria-label="Three women standing in front of green trees"></div>
    <h4>The VA Foundation Offices will be closed until further notice</h4><span class="date">APR 22, 2020</span>
  </article>
  <article class="post" style="left:768px">
    <div class="thumb" style="background:linear-gradient(160deg,#8b7f7a,#5a4a6a 50%,#d8d2cc)" role="img" aria-label="Staff member assisting a visitor at a desk"></div>
    <h4>Announcement: Corona Virus, Offices Closed to the Public 3/16 / 20-3 / 18/20</h4><span class="date">APR 22, 2020</span>
  </article>
  <div class="arrow" style="left:83px;top:2655px"><svg width="12" height="18"><path d="M10 2L3 9L10 16" stroke="#333" stroke-width="2" fill="none"/></svg></div>
  <div class="arrow" style="left:1071px;top:2655px"><svg width="12" height="18"><path d="M2 2L9 9L2 16" stroke="#333" stroke-width="2" fill="none"/></svg></div>
  <div class="abs divider"></div>
</section>

<section class="support">
  <h2 class="section-title center" style="top:3054px">Support our work</h2>
  <div class="partner" style="left:143px"><span style="background:#1e3a8a"></span></div>
  <div class="partner" style="left:329px"><span style="background:#c81e1e"></span></div>
  <div class="partner" style="left:514px"><span style="background:#2f6e2f;width:50px;border-radius:50%"></span></div>
  <div class="partner" style="left:700px"><span style="background:#8a1f1f;width:50px;border-radius:50%"></span></div>
  <div class="partner" style="left:886px"><span style="background:#222"></span></div>
  <div class="arrow" style="left:83px;top:3184px"><svg width="12" height="18"><path d="M10 2L3 9L10 16" stroke="#333" stroke-width="2" fill="none"/></svg></div>
  <div class="arrow" style="left:1071px;top:3184px"><svg width="12" height="18"><path d="M2 2L9 9L2 16" stroke="#333" stroke-width="2" fill="none"/></svg></div>
</section>

<section class="abs stories">
  <h3 class="sub-title" style="left:140px;top:84px">Worker and Member Stories</h3>
  <h3 class="sub-title" style="left:741px;top:84px">Follow us on Chirper</h3>
  <div class="panel" style="left:143px;top:142px;width:582px;height:237px">
    <div class="story" style="top:26px">
      <div class="avatar" style="background:#f0b400"></div>
      <div class="who">Mara Vell<span class="stars">★★★★★</span></div>
      <p>"Sed ut perspiciatis unde omnis iste natus error sit voluptatem accusantiumemque laudantium, totam remuae ab illo invenuae ab e ipsa quae ab illo inventore"</p>
    </div>
    <div class="story" style="top:124px">
      <div class="avatar" style="background:#c9c9c9"></div>
      <div class="who">John Doe<span class="stars">★★★★★</span></div>
      <p>"Sed ut perspiciatis unde omnis iste natus error sit voluptatem accusantiumemque laudantium, totam remuae ab illo invenuae ab e ipsa quae ab illo inventore"</p>
    </div>
    <div class="abs" style="left:570px;top:16px;width:4px;height:205px;background:#eee"><div style="width:4px;height:34px;margin-top:90px;background:#bbb"></div></div>
  </div>
  <div class="panel" style="left:743px;top:142px;width:312px;height:237px">
    <div class="abs" style="left:18px;top:18px;width:26px;height:26px;background:#b98a7a"></div>
    <div class="abs" style="left:56px;top:18px;font-size:10px;font-weight:700">Mara Vell <span style="font-weight:400;color:#888">@mvell</span></div>
    <div class="abs stars" style="left:48px;top:32px">★★★★★</div>
    <div class="abs" style="left:253px;top:20px;font-size:8px;color:#1d8ce0">Chirper</div>
    <p class="abs" style="left:18px;top:54px;width:280px;font-size:10px;line-height:19px;color:var(--text)">Our team kept the pantry open today and met many families; we thank each of you for the help.</p>
    <div class="abs" style="left:20px;top:98px;font-size:10px;color:#888">↶ &nbsp;&nbsp;&nbsp;&nbsp;&nbsp;&nbsp;&nbsp;&nbsp;&nbsp;&nbsp;&nbsp;⇄ 6 &nbsp;&nbsp;&nbsp;&nbsp;&nbsp;&nbsp;&nbsp;&nbsp;&nbsp;&nbsp;♥ 6</div>
    <div class="abs" style="left:18px;top:128px;width:276px;height:1px;background:var(--line)"></div>
    <div class="abs" style="left:24px;top:142px;font-size:9.5px;font-weight:500">write a comment</div>
    <div class="abs" style="left:22px;top:160px;width:270px;height:28px;border:1px solid var(--line);font-size:9px;color:#aaa;padding:8px">Post Your Comment Here</div>
  </div>
</section>

<footer class="abs footer">
  <div class="social" style="left:152px"></div>
  <div class="social" style="left:216px"></div>
  <div class="social" style="left:280px"></div>
  <div class="social" style="left:344px"></div>
  <div class="call">
    <svg width="44" height="44" viewBox="0 0 44 44"><circle cx="22" cy="22" r="20" fill="none" stroke="#d0141c" stroke-width="2.5"/><path d="M15 12c2-1 3 0 4 3l1 3c0 1-1 2-2 3 1 3 3 5 6 6 1-1 2-2 3-2l3 1c3 1 4 2 3 4-1 3-4 4-7 3-6-2-11-7-13-13-1-3 0-6 2-8z" fill="#d0141c"/></svg>
    <div><div class="small">Call Us</div><div class="num">1-800-555-0142</div></div>
  </div>
  <div class="brand light" style="left:810px;top:58px;font-size:30px"><span class="mark" style="width:20px;height:20px"></span>Valor Andes</div>
  <div class="foot-rule"></div>
  <nav class="footer-nav"><span>Home</span><span>Get Help Now</span><span>Take Action</span><span>News and Events</span><span>Support Our Work</span><span>About Us</span></nav>
  <div class="legal">© 2020 Valorandes.All rights reserved &nbsp;|&nbsp; Privacy Policy &nbsp;|&nbsp; Terms and Use</div>
</footer>

</body>
</html>
```